BRIGHTWAVE PARTNERS NAMECARD

Need to design a name card with an existing logo.

As we are professional corporate services provider our name card has to project a professional image.
Should be corporate, simple & professional.

Our corporate color is maroon red but not too dull.

Please refer to our website at www.brightwavepartners.com.sg

Would attach our logo herewith.

Front surface of namecard details:
BRIGHTWAVE PARTNERS PTE LTD
Registration No. 208731945K

Lowe Hui Ting CA (Singapore)
Director

Tel +65 6481 2957
Mobile +65 9172 3806
lowe@brightwavepartners.com.sg
www.brightwavepartners.com.sg

47 Palmer Lane
#07-14 Harbourlight Plaza
Singapore 274153

Back of namecard:-
OUR CORE SERVICES
Incorporation services
Corporate Secretarial Services
Accountancy service
Goods & Services Taxation
Corporate & Personal Taxation
Financial Reporting
Payroll Administration

AFFILIATES:
TRIVANTA CORPORATE SERVICES PTE LTD
BRIGHTWAVEREGISTRYPTE LTD
ORR MANAGEMENT SERVICES PTE LTD
DW LIM AND COMPANY PTE LTD
LEDGERWISE ACADEMY

```html
<!DOCTYPE html>
<html lang="en">
<head>
<meta charset="utf-8">
<title>Brightwave Partners Name Card</title>
<link href="https://fonts.googleapis.com/css2?family=Open+Sans:wght@400;600;700&display=swap" rel="stylesheet">
<style>
  :root {
    --brand-red: #c8102e;
    --card-dark: #222223;
    --card-black: #111112;
    --card-white: #f4f4f4;
    --text-light: #f2f2f2;
    --backdrop: #e6e3e0;
  }
  * { margin: 0; padding: 0; box-sizing: border-box; }
  html, body { width: 1200px; height: 900px; overflow: hidden; }
  body {
    background: var(--backdrop);
    font-family: "Open Sans", Arial, sans-serif;
    position: relative;
  }
  .card { position: absolute; overflow: hidden; box-shadow: 0 6px 18px rgba(0,0,0,.25); }

  /* Front */
  .card-front { left: 78px; top: 35px; width: 588px; height: 362px; background: var(--card-white); }
  .front-shapes { position: absolute; inset: 0; }
  .brand-name {
    position: absolute; right: 38px; top: 36px;
    color: var(--brand-red); font-weight: 700; font-size: 42px;
    line-height: 46px; text-align: right; letter-spacing: -0.5px;
  }
  .registration {
    position: absolute; left: 26px; top: 163px; color: #fff;
    font-size: 15px; font-weight: 600;
  }
  .registration span { font-weight: 400; }
  .holder { position: absolute; right: 36px; top: 195px; text-align: right; }
  .holder-name { color: var(--brand-red); font-size: 15px; font-weight: 600; line-height: 22px; }
  .holder-name span { font-weight: 400; }
  .holder-role { color: var(--text-light); font-size: 15px; line-height: 22px; }
  .address { position: absolute; left: 28px; top: 264px; color: var(--text-light); font-size: 15px; line-height: 27px; }
  .contacts { position: absolute; right: 20px; top: 256px; list-style: none; }
  .contacts li {
    display: flex; justify-content: flex-end; align-items: center; gap: 10px;
    color: var(--text-light); font-size: 14.5px; line-height: 21.5px;
  }
  .contacts svg { width: 10px; height: 10px; fill: var(--brand-red); }

  /* Back */
  .card-back { left: 389px; top: 505px; width: 566px; height: 352px; background: linear-gradient(135deg, #2a2a2b, var(--card-black)); }
  .back-edge { position: absolute; left: 0; top: 0; width: 28px; height: 100%; background: var(--card-black); }
  .back-band { position: absolute; left: 28px; top: 0; width: 127px; height: 100%; background: var(--brand-red); }
  .back-brand {
    position: absolute; left: 91px; top: 176px; width: 320px;
    transform: translate(-50%, -50%) rotate(-90deg);
    color: #fff; font-weight: 700; font-size: 38px; line-height: 44px; text-align: center;
  }
  .section-label {
    position: absolute; color: var(--brand-red); font-weight: 600;
    transform: rotate(-90deg); transform-origin: left top; white-space: nowrap;
  }
  .label-services { left: 190px; top: 180px; font-size: 13px; letter-spacing: .5px; }
  .label-affiliates { left: 192px; top: 312px; font-size: 17px; letter-spacing: 1px; }
  .service-list { position: absolute; left: 224px; top: 38px; list-style: none; }
  .service-list li {
    color: var(--text-light); font-size: 15px; line-height: 20.6px; padding-left: 15px; position: relative;
  }
  .service-list li::before {
    content: ""; position: absolute; left: 0; top: 7px; width: 7px; height: 7px;
    border-radius: 50%; background: var(--brand-red);
  }
  .affiliate-list { position: absolute; left: 223px; top: 212px; list-style: none; }
  .affiliate-list li { color: var(--text-light); font-size: 13px; line-height: 21.3px; }
</style>
</head>
<body>
  <section class="card card-front" aria-label="Name card front">
    <svg class="front-shapes" viewBox="0 0 588 362" width="588" height="362" aria-hidden="true">
      <polygon points="0,200 262,200 286,177 588,177 588,362 0,362" fill="var(--card-dark)"/>
      <polygon points="0,151 262,151 278,173 262,195 0,195" fill="var(--brand-red)"/>
    </svg>
    <div class="brand-name">BRIGHTWAVE<br>PARTNERS</div>
    <p class="registration">Registration No. <span>208731945K</span></p>
    <div class="holder">
      <p class="holder-name">Lowe Hui Ting CA <span>(Singapore)</span></p>
      <p class="holder-role">Director</p>
    </div>
    <address class="address">47 Palmer Lane<br>#07-14 Harbourlight Plaza<br>Singapore 274153</address>
    <ul class="contacts">
      <li>+65 6481 2957 <svg viewBox="0 0 10 10"><rect x="2" y="0" width="6" height="10" rx="1"/><rect x="3" y="1.5" width="4" height="6" fill="var(--card-dark)"/></svg></li>
      <li>+65 9172 3806 <svg viewBox="0 0 10 10"><path d="M0 3 Q5 0 10 3 L8 5 L6 4 L4 4 L2 5 Z"/><rect x="2" y="5" width="6" height="5"/></svg></li>
      <li>lowe@brightwavepartners.com.sg <svg viewBox="0 0 10 10"><rect x="0" y="2" width="10" height="7"/><path d="M0 2 L5 6 L10 2" stroke="var(--card-dark)" fill="none"/></svg></li>
      <li>www.brightwavepartners.com.sg <svg viewBox="0 0 10 10"><circle cx="5" cy="5" r="5"/></svg></li>
    </ul>
  </section>

  <section class="card card-back" aria-label="Name card back">
    <div class="back-edge"></div>
    <div class="back-band"></div>
    <div class="back-brand">BRIGHTWAVE<br>PARTNERS</div>
    <p class="section-label label-services">OUR CORE SERVICES</p>
    <ul class="service-list">
      <li>Incorporation Services</li>
      <li>Corporate Secretarial Services</li>
      <li>Accountancy Service</li>
      <li>Goods &amp; Services Taxation</li>
      <li>Corporate &amp; Personal Taxation</li>
      <li>Financial Reporting</li>
      <li>Payroll Administration</li>
    </ul>
    <p class="section-label label-affiliates">AFFILIATES</p>
    <ul class="affiliate-list">
      <li>TRIVANTA CORPORATE SERVICES PTE LTD</li>
      <li>BRIGHTWAVEREGISTRYPTE LTD</li>
      <li>ORR MANAGEMENT SERVICES PTE LTD</li>
      <li>DW LIM AND COMPANY PTE LTD</li>
      <li>LEDGERWISE ACADEMY</li>
    </ul>
  </section>
</body>
</html>
```